Brightvale Assist Public Benefit Corporation - Initial Website

We need to develop an initial website for Brightvale Assist PBC. We are a startup managed business services provider focused on small business owners, entrepreneurs and their employees. We are a public benefit corporation and our public mission is to help business owners, entrepreneurs and their employees overcome the challenges that hold them back from reaching personal and professional success.
Our primary service offerings are managed business services that allow us to support the day-to-day operations of the businesses we support. This ongoing support provides the necessary pre-requisite relationship so we can provide effective and timely support when their organizations are experiencing challenges and moments of crisis. In those moments, it is our opportunity to help them overcome those challenges and stay on track for business utopia.
Our services are provided on a contract basis for a fixed monthly fee. We want to build strong relationships that help our clients grow their businesses while taking away the stresses associated with the backend of the business operations.
Finally, our public benefit is that we provide crisis invention, critical incident support, and mental health services to business owners and their employees during challenging times in an effort to improve their overall quality of life.

Coding

Coded - Design and coding required

```html
<!DOCTYPE html>
<html lang="en">
<head>
<meta charset="utf-8">
<title>Brightvale Assist Public Benefit Corporation</title>
<link href="https://fonts.googleapis.com/css2?family=Poppins:wght@300;400;500;600;700;800&family=Roboto:wght@400;500;700&display=swap" rel="stylesheet">
<style>
:root{
  --orange:#ff7300;
  --navy:#0c1a4a;
  --navy-deep:#071338;
  --ink:#111111;
  --grey:#6b6b6b;
  --card:#f3f3f3;
  --white:#ffffff;
  --black:#000000;
}
*{margin:0;padding:0;box-sizing:border-box}
html,body{width:1200px;height:3794px;overflow:hidden;background:var(--white)}
body{font-family:"Roboto",sans-serif;color:var(--ink);position:relative}
.abs{position:absolute}
.heading{font-family:"Poppins",sans-serif}
.btn{position:absolute;display:flex;align-items:center;justify-content:center;gap:8px;border-radius:30px;background:var(--orange);color:var(--white);font-family:"Roboto",sans-serif;font-weight:700;font-size:13px;letter-spacing:.2px}
.btn .dot{width:13px;height:13px;border-radius:50%;background:var(--white);display:inline-flex;align-items:center;justify-content:center}
.btn .dot svg{width:7px;height:7px}

/* header */
.brand{left:141px;top:18px;font-family:"Poppins",sans-serif;color:var(--navy)}
.brand .name{font-size:38px;font-weight:400;color:var(--orange);line-height:40px;letter-spacing:-.5px}
.brand .sub{font-size:16px;font-weight:600;line-height:18px;letter-spacing:.3px}
.call-icon{left:624px;top:11px;width:44px;height:44px;border-radius:50%;background:var(--navy)}
.call-label{left:678px;top:14px;font-size:11px;color:var(--grey)}
.call-number{left:678px;top:33px;font-size:15px;font-weight:500;color:var(--ink)}
.nav{left:0;top:80px;width:1200px;height:20px}
.nav a{position:absolute;font-size:13px;font-weight:700;color:var(--ink);text-decoration:none}
.nav a.active{color:var(--orange)}

/* hero */
.hero{left:0;top:112px;width:1200px;height:530px;background:linear-gradient(100deg,#1c2b45 0%,#5a4232 35%,#8a6a55 55%,#3f5365 80%,#7a8d99 100%)}
.hero-title{left:0;width:1200px;text-align:center;color:var(--white);font-family:"Poppins",sans-serif;font-weight:700}

/* about */
.about-photo{left:180px;top:690px;width:382px;height:382px;border-radius:50%;background:linear-gradient(135deg,#8fa3b8,#4a5c70 60%,#2e3c4f);box-shadow:0 10px 30px rgba(0,0,0,.18);border:4px solid var(--white)}
.badge{left:454px;top:947px;width:132px;height:132px;border-radius:50%;background:var(--navy);border:6px solid var(--white);box-shadow:0 6px 20px rgba(0,0,0,.2);color:var(--white);text-align:center}
.badge b{display:block;font-family:"Poppins",sans-serif;font-size:36px;font-weight:600;line-height:40px;margin-top:24px}
.badge span{font-size:11px;line-height:17px}
.sec-title{font-family:"Poppins",sans-serif;font-size:35px;color:var(--ink);font-weight:400}
.sec-title b{font-weight:800}
.para{font-size:15px;line-height:25px;color:var(--grey)}

/* services */
.services{left:0;top:1149px;width:1200px;height:636px;background:linear-gradient(90deg,#0e2a5c 0%,#0b2452 50%,#0a1d45 100%)}
.services-visual{left:600px;top:1149px;width:600px;height:636px;background:radial-gradient(ellipse at 55% 55%,#2a4a78 0%,#14305f 45%,#0a1d45 80%)}
.svc-icon{width:80px;height:80px;border-radius:50%;background:var(--white);border:5px solid #c8d0de;display:flex;align-items:center;justify-content:center}
.svc-icon.hot{background:var(--orange);border-color:#f6b88a}
.svc-title{font-size:16px;font-weight:700;color:var(--white)}
.svc-text{font-size:13px;line-height:24px;color:var(--white)}
.price{left:929px;top:1359px;width:175px;height:84px;background:var(--white);border-radius:4px;display:flex;align-items:center;justify-content:center;color:var(--navy);font-family:"Poppins",sans-serif}
.note{left:605px;top:1565px;width:205px;height:84px;background:var(--white);border-radius:4px;padding:13px 12px;font-size:13px;line-height:21px;color:var(--grey)}

/* testimonials */
.t-card{background:var(--card);border-radius:6px}
.t-card.lead{background:var(--white);box-shadow:0 6px 24px rgba(0,0,0,.12)}
.avatar{border-radius:50%;background:linear-gradient(160deg,#7d8fa3,#2c3a4f)}
.t-name{font-weight:700;color:var(--ink)}
.t-city{color:var(--ink)}
.t-text{color:var(--grey)}
.arrow{width:50px;height:50px;border-radius:50%;display:flex;align-items:center;justify-content:center}
.arrow.light{background:var(--white);box-shadow:0 3px 12px rgba(0,0,0,.15)}
.arrow.dark{background:var(--navy)}

/* cta */
.cta{left:0;top:2281px;width:1200px;height:361px;background:var(--orange);color:var(--white);text-align:center}
.cta h2{font-family:"Poppins",sans-serif;font-weight:700;font-size:35px;line-height:54px;letter-spacing:.3px}
.cta h2 span{font-weight:500}
.cta p{font-size:14px;line-height:25px}
.cta-btn{left:485px;top:246px;width:232px;height:45px;background:var(--white);border:3px solid var(--navy);color:var(--navy);border-radius:30px;display:flex;align-items:center;justify-content:center;gap:8px;font-weight:700;font-size:13px}

/* blog */
.b-card{top:2791px;width:296px;height:397px;background:var(--white);border-radius:12px;box-shadow:0 4px 20px rgba(0,0,0,.09)}
.b-img{position:absolute;left:9px;top:10px;width:278px;height:174px;border-radius:10px}
.b-date{position:absolute;left:79px;top:166px;width:138px;height:34px;background:var(--navy);color:var(--white);border-radius:8px 8px 0 0;font-family:"Poppins",sans-serif;font-weight:600;font-size:15px;display:flex;align-items:center;justify-content:center}
.b-title{position:absolute;left:19px;top:226px;font-size:16px;line-height:26px;font-weight:700;color:var(--ink)}
.b-text{position:absolute;left:19px;top:286px;font-size:15px;line-height:26px;color:var(--grey)}
.b-more{position:absolute;left:19px;top:352px;font-size:15px;font-weight:700;color:var(--orange);display:flex;align-items:center;gap:7px}
.b-more i{width:13px;height:13px;border-radius:50%;background:var(--orange);display:inline-flex;align-items:center;justify-content:center}

/* footer */
.footer{left:0;top:3340px;width:1200px;height:454px;background:var(--black);color:var(--white)}
.f-head{font-size:14px;font-weight:700}
.f-rule{width:48px;height:2px;background:var(--orange);position:absolute;top:26px;left:0}
.f-rule::before{content:"";position:absolute;left:0;top:-3px;width:8px;height:8px;border-radius:50%;background:var(--orange)}
.f-list{list-style:none;font-size:13px;line-height:25px;position:absolute;top:50px;left:0;white-space:nowrap}
.f-icon{width:30px;height:30px;border-radius:50%;background:var(--white);display:flex;align-items:center;justify-content:center}
.social{width:34px;height:34px;border-radius:50%;background:var(--white)}
</style>
</head>
<body>

<!-- Header -->
<div class="abs brand">
  <div class="name">Brightvale Assist</div>
  <div class="sub">PUBLIC BENEFIT CORPORATION</div>
</div>
<div class="abs call-icon">
  <svg width="44" height="44" viewBox="0 0 44 44"><path d="M16 13c1.5-1 3 2 3.5 3.5.4 1.3-1.8 2-1.3 3.3a12 12 0 0 0 6 6c1.3.5 2-1.7 3.3-1.3 1.5.5 4.5 2 3.5 3.5-1.5 2.3-3.5 3.5-6.5 2a18 18 0 0 1-9.5-9.5c-1.5-3 0-5 1-7.5z" fill="none" stroke="#fff" stroke-width="1.6"/></svg>
</div>
<div class="abs call-label">Call Us Today</div>
<div class="abs call-number">+1 (555) 014 2290</div>
<div class="btn" style="left:831px;top:12px;width:223px;height:41px;">BOOK A CONSULTATION <span class="dot"><svg viewBox="0 0 8 8"><path d="M3 1.5 5.5 4 3 6.5" stroke="#ff7300" stroke-width="1.6" fill="none"/></svg></span></div>
<nav class="abs nav">
  <a class="active" style="left:485px">HOME</a>
  <a style="left:549px">ABOUT US</a>
  <a style="left:638px">OUR SERVICES</a>
  <a style="left:751px">OUR APPROACH</a>
  <a style="left:874px">RESOURCES</a>
  <a style="left:971px">CONTACT US</a>
</nav>
<div class="abs" style="left:0;top:110px;width:1200px;height:1px;background:#dddddd"></div>

<!-- Hero -->
<div class="abs hero" role="img" aria-label="Photo of two business people shaking hands over a glowing financial chart backdrop"></div>
<div class="abs hero-title" style="top:248px;font-size:38px;">EMPOWERING SMALL BUSINESSES</div>
<div class="abs hero-title" style="top:297px;font-size:48px;">TO THRIVE IN EVERY CHALLENGE</div>
<div class="btn" style="left:523px;top:386px;width:155px;height:41px;">GET STARTED <span class="dot"><svg viewBox="0 0 8 8"><path d="M3 1.5 5.5 4 3 6.5" stroke="#ff7300" stroke-width="1.6" fill="none"/></svg></span></div>
<svg class="abs" style="left:0;top:500px" width="1200" height="150" viewBox="0 0 1200 150">
  <path d="M40 100 C250 10 450 30 640 100 C800 150 1000 130 1200 60 L1200 80 C1030 150 820 170 640 125 C460 80 250 50 40 100 Z" fill="#0c1a4a"/>
  <path d="M0 115 C180 20 420 20 620 95 C800 150 1000 135 1200 70 L1200 150 L0 150 Z" fill="#ffffff"/>
</svg>
<div class="abs" style="left:575px;top:561px;width:50px;height:50px;border-radius:50%;background:#fff;box-shadow:0 3px 12px rgba(0,0,0,.2);display:flex;align-items:center;justify-content:center">
  <svg width="14" height="14" viewBox="0 0 14 14"><path d="M3 3l4 4 4-4M3 7l4 4 4-4" fill="none" stroke="#0c1a4a" stroke-width="1.6"/></svg>
</div>

<!-- About -->
<div class="abs about-photo" role="img" aria-label="Photo of two smiling colleagues shaking hands in an office"></div>
<div class="abs badge"><b>25</b><span>Years Of<br>Experience</span></div>
<h2 class="abs sec-title" style="left:664px;top:710px;"><b>ABOUT</b> US</h2>
<p class="abs para" style="left:664px;top:768px;width:345px;">Lorem ipsum dolor sit amet, consectetur adipiscing elit, sed do eiusmod tempor incididunt ut labore et dolore magna aliqua. Ut enim ad minim veniam, quis Lorem ipsum dolor sit amet,</p>
<h3 class="abs" style="left:664px;top:882px;font-size:20px;font-weight:500;color:var(--navy);letter-spacing:.2px">MISSION STATEMENT</h3>
<p class="abs para" style="left:664px;top:921px;width:345px;">Lorem ipsum dolor sit amet, consectetur adipiscing elit, sed do eiusmod tempor incididunt ut labore et dolore magna aliqua.</p>
<div class="btn" style="left:664px;top:1020px;width:156px;height:42px;">LEARN MORE <span class="dot"><svg viewBox="0 0 8 8"><path d="M3 1.5 5.5 4 3 6.5" stroke="#ff7300" stroke-width="1.6" fill="none"/></svg></span></div>

<!-- Services -->
<div class="abs services"></div>
<div class="abs services-visual" role="img" aria-label="Photo of an open hand beneath a glowing rising bar and line chart"></div>
<h2 class="abs sec-title" style="left:146px;top:1264px;color:#fff;"><b>OUR</b> SERVICES</h2>

<div class="abs svc-icon" style="left:144px;top:1340px;">
  <svg width="42" height="42" viewBox="0 0 42 42" fill="none" stroke="#0c1a4a" stroke-width="1.8"><circle cx="17" cy="15" r="6"/><path d="M6 34c0-7 5-11 11-11s9 3 10 6"/><circle cx="30" cy="28" r="5"/><path d="M30 20v3M30 33v3M22 28h3M35 28h3"/></svg>
</div>
<div class="abs svc-title" style="left:237px;top:1346px;">MANAGED BUSINESS SERVICE</div>
<div class="abs svc-text" style="left:237px;top:1372px;width:330px;">Lorem ipsum dolor sit amet, consectetur adipiscing elit, sed do eiusmod tempor incididunt</div>

<div class="abs svc-icon" style="left:144px;top:1456px;">
  <svg width="42" height="42" viewBox="0 0 42 42" fill="none" stroke="#0c1a4a" stroke-width="1.8"><rect x="10" y="7" width="20" height="28" rx="2"/><path d="M14 14h12M14 19h12M14 24h8M30 12h4v26H14v-3"/></svg>
</div>
<div class="abs svc-title" style="left:237px;top:1462px;">CRISIS INTERVENTION</div>
<div class="abs svc-text" style="left:237px;top:1488px;width:330px;">Lorem ipsum dolor sit amet, consectetur adipiscing elit, sed do eiusmod tempor incididunt</div>

<div class="abs svc-icon hot" style="left:144px;top:1571px;">
  <svg width="42" height="42" viewBox="0 0 42 42" fill="none" stroke="#fff" stroke-width="1.8"><path d="M14 22v-6M19 22V10M24 22v-9M29 22v-4"/><path d="M6 28l8-4h10a2 2 0 0 1 0 4h-7M6 34l6-2h12l10-8"/></svg>
</div>
<div class="abs svc-title" style="left:237px;top:1577px;">EMPLOYEE &amp; OWNER WELLNESS</div>
<div class="abs svc-text" style="left:237px;top:1603px;width:330px;">Lorem ipsum dolor sit amet, consectetur adipiscing elit, sed do eiusmod tempor incididunt</div>
<div class="abs" style="left:238px;top:1662px;font-size:13px;color:#fff;text-decoration:underline">View More</div>

<div class="abs price"><span style="font-size:25px;font-weight:600">$ 225</span><span style="font-size:21px;margin:0 5px">/</span><span style="font-size:18px;font-weight:500">month</span></div>
<div class="abs note">Our services are provided on a contract basis for a fixed monthly fee</div>

<!-- Testimonials -->
<h2 class="abs sec-title" style="left:0;width:1200px;text-align:center;top:1866px;"><b>OUR</b> TESTIMONIALS</h2>

<div class="abs t-card" style="left:146px;top:1973px;width:268px;height:214px;">
  <div class="abs avatar" role="img" aria-label="Portrait of client" style="left:24px;top:16px;width:66px;height:66px;"></div>
  <div class="abs t-name" style="left:115px;top:35px;font-size:12px;">DANA PIERCE</div>
  <div class="abs t-city" style="left:115px;top:54px;font-size:11px;">Lorum Ipsum City</div>
  <p class="abs t-text" style="left:21px;top:96px;width:230px;font-size:11px;line-height:20px;">Lorem ipsum dolor sit amet, consectetur adipisc ing elit, sed do eiusmod tempor incididunt ut labore et dolore magna aliqua. Ut enim ad minim veniam, quis nostrud exercitation ullamco laboris.</p>
</div>
<div class="abs t-card lead" style="left:442px;top:1954px;width:316px;height:248px;">
  <div class="abs avatar" role="img" aria-label="Portrait of client" style="left:29px;top:18px;width:78px;height:78px;"></div>
  <div class="abs t-name" style="left:134px;top:42px;font-size:14px;">DANA PIERCE</div>
  <div class="abs t-city" style="left:134px;top:66px;font-size:13px;">Lorum Ipsum City</div>
  <p class="abs t-text" style="left:26px;top:112px;width:272px;font-size:13.5px;line-height:24px;">Lorem ipsum dolor sit amet, consectetur adipisc ing elit, sed do eiusmod tempor incididunt ut labore et dolore magna aliqua. Ut enim ad minim veniam, quis nostrud exercitation ullamco laboris.</p>
</div>
<div class="abs t-card" style="left:788px;top:1973px;width:266px;height:214px;">
  <div class="abs avatar" role="img" aria-label="Portrait of client" style="left:22px;top:16px;width:66px;height:66px;"></div>
  <div class="abs t-name" style="left:112px;top:35px;font-size:12px;">DANA PIERCE</div>
  <div class="abs t-city" style="left:112px;top:54px;font-size:11px;">Lorum Ipsum City</div>
  <p class="abs t-text" style="left:20px;top:96px;width:230px;font-size:11px;line-height:20px;">Lorem ipsum dolor sit amet, consectetur adipisc ing elit, sed do eiusmod tempor incididunt ut labore et dolore magna aliqua. Ut enim ad minim veniam, quis nostrud exercitation ullamco laboris.</p>
</div>
<div class="abs arrow light" style="left:71px;top:2053px;"><svg width="14" height="14" viewBox="0 0 14 14"><path d="M7 3L3 7l4 4M11 3L7 7l4 4" fill="none" stroke="#0c1a4a" stroke-width="1.6"/></svg></div>
<div class="abs arrow dark" style="left:1079px;top:2053px;"><svg width="14" height="14" viewBox="0 0 14 14"><path d="M3 3l4 4-4 4M7 3l4 4-4 4" fill="none" stroke="#fff" stroke-width="1.6"/></svg></div>

<!-- Call to action -->
<section class="abs cta">
  <h2 style="padding-top:52px">READY TO RELIEVE THE STRESS OF<br><span>BUSINESS OPERATIONS?&nbsp; LET’S TALK</span></h2>
  <p style="margin-top:10px">Lorem ipsum dolor sit amet, consectetur adipiscing elit, sed do eiusmod tempor incididunt ut labore et dolore magna aliqua.<br>Ut enim ad minim veniam, quis nostrud exercitation ullamco laboris nisi ut aliquip ex e</p>
  <div class="abs cta-btn">BOOK A CONSULTATION <svg width="13" height="13" viewBox="0 0 13 13"><circle cx="6.5" cy="6.5" r="6.5" fill="#0c1a4a"/><path d="M5 3.5l3 3-3 3" stroke="#fff" stroke-width="1.5" fill="none"/></svg></div>
</section>

<!-- Blog -->
<h2 class="abs sec-title" style="left:0;width:1200px;text-align:center;top:2727px;"><b>OUR</b> BLOG</h2>

<article class="abs b-card" style="left:124px;">
  <div class="b-img" role="img" aria-label="Photo of two colleagues reviewing a laptop together" style="background:linear-gradient(135deg,#a9b6c2,#5e6e7e)"></div>
  <div class="b-date">OCT 22,2024</div>
  <div class="b-title">LOREM IPSUM DOLOR SIT AMET,<br>CONSECTETUR ADIPISCING</div>
  <div class="b-text">Sed ut perspiciatis unde omnis iste<br>natus error sit voluptatem</div>
  <div class="b-more">LEARN MORE <i><svg width="7" height="7" viewBox="0 0 8 8"><path d="M3 1.5 5.5 4 3 6.5" stroke="#fff" stroke-width="1.6" fill="none"/></svg></i></div>
</article>
<article class="abs b-card" style="left:442px;">
  <div class="b-img" role="img" aria-label="Photo of a team meeting in a city-view office" style="background:linear-gradient(135deg,#6d8396,#2f3f50)"></div>
  <div class="b-date">OCT 22,2024</div>
  <div class="b-title">LOREM IPSUM DOLOR SIT AMET,<br>CONSECTETUR ADIPISCING</div>
  <div class="b-text">Sed ut perspiciatis unde omnis iste<br>natus error sit voluptatem</div>
  <div class="b-more">LEARN MORE <i><svg width="7" height="7" viewBox="0 0 8 8"><path d="M3 1.5 5.5 4 3 6.5" stroke="#fff" stroke-width="1.6" fill="none"/></svg></i></div>
</article>
<article class="abs b-card" style="left:758px;">
  <div class="b-img" role="img" aria-label="Photo of two professionals talking in an office" style="background:linear-gradient(135deg,#c8b9a8,#5d5a5e)"></div>
  <div class="b-date">OCT 22,2024</div>
  <div class="b-title">LOREM IPSUM DOLOR SIT AMET,<br>CONSECTETUR ADIPISCING</div>
  <div class="b-text">Sed ut perspiciatis unde omnis iste<br>natus error sit voluptatem</div>
  <div class="b-more">LEARN MORE <i><svg width="7" height="7" viewBox="0 0 8 8"><path d="M3 1.5 5.5 4 3 6.5" stroke="#fff" stroke-width="1.6" fill="none"/></svg></i></div>
</article>
<div class="abs arrow light" style="left:71px;top:2975px;"><svg width="14" height="14" viewBox="0 0 14 14"><path d="M7 3L3 7l4 4M11 3L7 7l4 4" fill="none" stroke="#0c1a4a" stroke-width="1.6"/></svg></div>
<div class="abs arrow dark" style="left:1079px;top:2975px;"><svg width="14" height="14" viewBox="0 0 14 14"><path d="M3 3l4 4-4 4M7 3l4 4-4 4" fill="none" stroke="#fff" stroke-width="1.6"/></svg></div>

<!-- Footer -->
<svg class="abs" style="left:0;top:3240px" width="1200" height="110" viewBox="0 0 1200 110">
  <path d="M40 75 C200 10 420 0 620 45 C820 90 1000 80 1200 10 L1200 30 C1010 100 820 110 620 70 C420 30 200 30 40 75 Z" fill="#0c1a4a"/>
  <path d="M0 95 C180 25 420 20 620 60 C820 100 1010 90 1200 25 L1200 110 L0 110 Z" fill="#000"/>
</svg>
<footer class="abs footer">
  <div class="abs" style="left:146px;top:54px;font-family:'Poppins',sans-serif;">
    <div style="font-size:50px;font-weight:300;line-height:54px;letter-spacing:-.5px">Brightvale Assist</div>
    <div style="font-size:22px;font-weight:600;line-height:26px;letter-spacing:.5px">PUBLIC BENEFIT CORPORATION</div>
  </div>

  <div class="abs" style="left:143px;top:180px;">
    <div class="f-head">QUICK LINKS</div><div class="f-rule"></div>
    <ul class="f-list"><li>Home</li><li>About Us</li><li>Our Services</li><li>Our Approach</li><li>Resources</li><li>Contact Us</li></ul>
  </div>
  <div class="abs" style="left:399px;top:180px;">
    <div class="f-head">OTHER LINKS</div><div class="f-rule"></div>
    <ul class="f-list"><li>Testimonials</li><li>Why Choose Us</li><li>Our Blog</li><li>Our Mission</li></ul>
  </div>
  <div class="abs" style="left:639px;top:180px;width:260px;height:200px;">
    <div class="f-head">CONTACT US</div><div class="f-rule"></div>
    <div class="abs f-icon" style="left:1px;top:56px;"><svg width="14" height="14" viewBox="0 0 14 14"><path d="M7 13s4.5-4.5 4.5-7.5a4.5 4.5 0 0 0-9 0C2.5 8.5 7 13 7 13z" fill="#0c1a4a"/><circle cx="7" cy="5.5" r="1.6" fill="#fff"/></svg></div>
    <div class="abs" style="left:47px;top:54px;font-size:13px;line-height:25px;white-space:nowrap">123, Lorum Ipsum Dolor,<br>Sit Amet . USA.</div>
    <div class="abs f-icon" style="left:1px;top:113px;"><svg width="14" height="14" viewBox="0 0 14 14"><path d="M3.5 1.5c1-.6 2 1.3 2.2 2.2.2.8-1.1 1.2-.8 2a7.5 7.5 0 0 0 3.8 3.8c.8.3 1.2-1 2-.8.9.2 2.8 1.2 2.2 2.2-1 1.5-2.3 2.2-4.2 1.3A11 11 0 0 1 2.5 6.2c-.9-1.9-.2-3.3 1-4.7z" fill="#0c1a4a"/></svg></div>
    <div class="abs" style="left:47px;top:119px;font-size:13px;white-space:nowrap">+1 (555) 014 2290</div>
    <div class="abs f-icon" style="left:1px;top:154px;"><svg width="14" height="14" viewBox="0 0 14 14"><rect x="1.5" y="3" width="11" height="8" rx="1" fill="#0c1a4a"/><path d="M1.5 3.5 7 7.5l5.5-4" stroke="#fff" stroke-width="1" fill="none"/></svg></div>
    <div class="abs" style="left:47px;top:161px;font-size:13px;white-space:nowrap">info@brightvaleassist.example</div>
  </div>
  <div class="abs" style="left:935px;top:180px;width:180px;height:150px;">
    <div class="f-head">OUR NEWSLETTER</div><div class="f-rule"></div>
    <div class="abs" style="left:-6px;top:60px;width:180px;height:40px;border-radius:20px;background:#fff;"></div>
    <div class="abs" style="left:9px;top:73px;font-size:11px;color:#777;">Email Address</div>
    <div class="abs" style="left:134px;top:64px;width:32px;height:32px;border-radius:50%;background:var(--navy);display:flex;align-items:center;justify-content:center"><svg width="10" height="10" viewBox="0 0 10 10"><path d="M2 2l3 3-3 3M5 2l3 3-3 3" fill="none" stroke="#fff" stroke-width="1.3"/></svg></div>
    <div class="abs social" style="left:5px;top:123px;" aria-label="Social profile"></div>
    <div class="abs social" style="left:46px;top:123px;" aria-label="Social profile"></div>
    <div class="abs social" style="left:87px;top:123px;" aria-label="Social profile"></div>
  </div>

  <div class="abs" style="left:143px;top:400px;width:912px;height:1px;background:#333"></div>
  <div class="abs" style="left:0;width:1200px;text-align:center;top:420px;font-size:11px;">Copyright@2024 - All Rights Reserved</div>
</footer>

</body>
</html>
```